Dunwoody Business Card Design

Small Company
looking to ramp up work need business cards sick of everyone asking for a card
client base is broad.
keep it simple
Just want on the reverse of the card somewhere for me to write details for clients
appointments etc..
want to use the phrase
"Your safe, reliable and trust worthy Tradesmen"

Industry/Entity Type

Business

Contact Information for Business Card

Dunwoody Electrical Solutions Pty Ltd
Director Bradley Dunwoody
email - dunwoodyelectricalsolutions@voltmail.example
Ph - 03 95551827
Mobile - 0491570386
Domestic, Industrial, Commercial & Mining
Electrical, Solar, Communications & Fibre
REC: 58104

```html
<!DOCTYPE html>
<html lang="en">
<head>
<meta charset="utf-8">
<title>Dunwoody Electrical Solutions – Business Card</title>
<link href="https://fonts.googleapis.com/css2?family=Questrial&display=swap" rel="stylesheet">
<style>
  :root {
    --navy: #27348b;
    --red: #e3262b;
    --card: #ffffff;
    --stage: #eceef1;
    --rule: #5a64a8;
    --faint-navy: rgba(39, 52, 139, 0.10);
  }
  * { box-sizing: border-box; margin: 0; padding: 0; }
  html, body {
    width: 1200px; height: 784px; overflow: hidden;
    background: var(--stage);
    font-family: "Questrial", "Century Gothic", sans-serif;
  }
  .stage { position: relative; width: 1200px; height: 784px; }
  .card {
    position: absolute; width: 540px; height: 330px;
    background: var(--card);
    box-shadow: 0 2px 10px rgba(0,0,0,0.12);
    overflow: hidden;
  }

  /* Reverse side: notes card */
  .card--reverse { left: 40px; top: 70px; }
  .services {
    position: absolute; top: 26px; left: 0; right: 0;
    text-align: center; color: var(--navy);
    font-size: 14px; line-height: 17px; letter-spacing: 0.2px;
  }
  .licence { color: var(--red); font-size: 11px; line-height: 15px; margin-top: 1px; }
  .watermark {
    position: absolute; left: 0; right: 0; top: 122px;
    text-align: center;
    color: var(--faint-navy); font-size: 72px; line-height: 1;
  }
  .note-lines { position: absolute; left: 36px; right: 36px; top: 96px; }
  .note-line {
    height: 0; border-top: 1.5px dashed var(--rule);
    margin-bottom: 26px;
  }

  /* Front side */
  .card--front { left: 620px; top: 384px; }
  .holder {
    position: absolute; top: 26px; right: 28px; text-align: right;
  }
  .holder-name { color: var(--navy); font-size: 15px; }
  .holder-role { color: var(--red); font-size: 12px; margin-top: 2px; }

  .company {
    position: absolute; left: 34px; top: 78px;
    color: var(--navy);
  }
  .company-name { font-size: 50px; line-height: 1; }
  .company-sub { font-size: 19px; line-height: 24px; letter-spacing: 0.5px; margin-top: 4px; }

  .accent-rule {
    position: absolute; left: 0; right: 0; top: 170px; height: 6px;
    background: var(--red);
  }
  .email-top {
    position: absolute; right: 26px; top: 188px;
    color: var(--navy); font-size: 14px;
  }
  .tagline-band {
    position: absolute; left: 0; right: 0; top: 214px; height: 24px;
    background: var(--red); color: #fff;
    font-size: 14px; letter-spacing: 2px; line-height: 24px;
    padding-left: 34px;
  }
  .contacts { position: absolute; left: 34px; top: 250px; list-style: none; }
  .contact {
    display: flex; align-items: center; gap: 8px;
    color: var(--navy); font-size: 18px; line-height: 23px;
  }
  .contact svg { width: 18px; height: 18px; flex: none; }
</style>
</head>
<body>
<main class="stage">

  <section class="card card--reverse" aria-label="Card reverse with notes lines">
    <div class="services">
      Domestic, Industrial, Commercial &amp; Mining Electrical,<br>
      Solar, Communications &amp; Fibre
      <div class="licence">REC: 58104</div>
    </div>
    <div class="watermark" aria-hidden="true">Dunwoody</div>
    <div class="note-lines" aria-hidden="true">
      <div class="note-line"></div><div class="note-line"></div>
      <div class="note-line"></div><div class="note-line"></div>
      <div class="note-line"></div><div class="note-line"></div>
      <div class="note-line"></div><div class="note-line"></div>
    </div>
  </section>

  <section class="card card--front" aria-label="Card front">
    <div class="holder">
      <div class="holder-name">Bradley Dunwoody</div>
      <div class="holder-role">Director</div>
    </div>

    <div class="company">
      <div class="company-name">Dunwoody</div>
      <div class="company-sub">Electrical Solutions</div>
    </div>

    <div class="accent-rule" aria-hidden="true"></div>

    <div class="email-top">dunwoodyelectricalsolutions@voltmail.example</div>

    <div class="tagline-band">Your safe, reliable and trust worthy Tradesmen</div>

    <ul class="contacts">
      <li class="contact">
        <svg viewBox="0 0 24 24" aria-hidden="true"><path fill="#e3262b" d="M6.6 10.8a15 15 0 0 0 6.6 6.6l2.2-2.2a1 1 0 0 1 1-.25 11.4 11.4 0 0 0 3.6.57 1 1 0 0 1 1 1V20a1 1 0 0 1-1 1A17 17 0 0 1 3 4a1 1 0 0 1 1-1h3.5a1 1 0 0 1 1 1c0 1.25.2 2.45.57 3.57a1 1 0 0 1-.25 1z"/></svg>
        03 95551827
      </li>
      <li class="contact">
        <svg viewBox="0 0 24 24" aria-hidden="true"><rect x="6" y="2" width="12" height="20" rx="2" fill="#e3262b"/><rect x="8" y="5" width="8" height="10" fill="#fff"/><circle cx="12" cy="18.5" r="1.3" fill="#fff"/></svg>
        0491570386
      </li>
      <li class="contact">
        <svg viewBox="0 0 24 24" aria-hidden="true"><rect x="2" y="5" width="20" height="14" rx="1.5" fill="#e3262b"/><path d="M3 6.5l9 6.5 9-6.5" fill="none" stroke="#fff" stroke-width="1.6"/></svg>
        dunwoodyelectricalsolutions@voltmail.example
      </li>
    </ul>
  </section>

</main>
</body>
</html>
```